Tranquil Pathway Business Card

Logo attached. (will be printing onto thick white/off white textured card)

Double sided business card for two Therapists working at Tranquil Pathway.

Require one design, but with different name and mobile numbers on each card.

Target Market(s)

Medical, Health

Industry/Entity Type

Business

Contact Information for Business Card

Need one business card design, but a separate card for each person - Colin Marchetti and Marieke de Boeckx.

FRONT OF CARD

Logo

Name (Colin Marchetti on one card, Marieke de Boeckx on the other)
Professional Clinical Hypnotherapist

Consulting Rooms (Near Lindqvist Hospital)
482 Brackenfield Road
Dunmore VIC 3987

Colin@TranquilPathway.example.au OR Marieke@TranquilPathway.example.au

Mobile: 0455 872 604 (for Colin) OR
Mobile: 0467 290 518 (for Marieke)

BACK OF CARD

Logo

Website: www.TranquilPathway.example.au

Phone: 1300 958 471

Requirements
Must have
• Text and logo only. No additiional graphics.

```html
<!DOCTYPE html>
<html lang="en">
<head>
<meta charset="utf-8">
<title>Tranquil Pathway Business Cards</title>
<link rel="stylesheet" href="https://fonts.googleapis.com/css2?family=Alegreya+Sans:wght@400;500;700&display=swap">
<style>
  :root {
    --page: #ffffff;
    --card-blue: #17799d;
    --band-grey: #5f7f8e;
    --band-dark: #23272b;
    --band-black: #050506;
    --text-light: #ffffff;
    --brand-navy: #2b3367;
    --mark-ring: #6b6e73;
    --divider: #6d6f73;
  }
  * { box-sizing: border-box; margin: 0; padding: 0; }
  html, body {
    width: 1200px; height: 782px; overflow: hidden;
    background: var(--page);
    font-family: "Alegreya Sans", sans-serif;
  }
  .sheet { position: relative; width: 1200px; height: 782px; }
  .card {
    position: absolute; width: 573px; height: 316px; overflow: hidden;
    color: var(--text-light);
    background: linear-gradient(to bottom,
      var(--card-blue) 0%, var(--card-blue) 63%,
      var(--band-grey) 68%, var(--band-dark) 88%, var(--band-black) 100%);
  }
  .card--front-a { left: 16px;  top: 67px; }
  .card--back-a  { left: 615px; top: 67px; width: 571px; }
  .card--front-b { left: 16px;  top: 413px; }
  .card--back-b  { left: 615px; top: 413px; width: 571px; }

  .brand { position: absolute; display: flex; align-items: center; }
  .brand__dot {
    border-radius: 50%;
    background: var(--brand-navy);
    border: 4px solid var(--mark-ring);
    flex: none;
  }
  .brand__rule { background: var(--divider); flex: none; }
  .brand__name { color: var(--brand-navy); font-weight: 700; letter-spacing: 0.5px; white-space: nowrap; }

  .brand--small { left: 12px; top: 12px; }
  .brand--small .brand__dot { width: 54px; height: 54px; border-width: 3px; }
  .brand--small .brand__rule { width: 1px; height: 52px; margin: 0 8px 0 6px; }
  .brand--small .brand__name { font-size: 19px; }

  .brand--large { left: 100px; top: 72px; }
  .brand--large .brand__dot { width: 118px; height: 118px; border-width: 7px; }
  .brand--large .brand__rule { width: 2px; height: 112px; margin: 0 14px 0 12px; }
  .brand--large .brand__name { font-size: 36px; }

  .holder { position: absolute; left: 0; right: 0; top: 112px; text-align: center; }
  .holder__name { font-size: 37px; font-weight: 400; line-height: 1.1; }
  .holder__role { font-size: 18px; margin-top: 4px; }

  .contact { position: absolute; font-size: 12px; line-height: 1.6; }
  .contact--personal { left: 12px; top: 252px; }
  .contact--personal p + p { margin-top: 4px; }
  .contact--rooms { right: 12px; top: 253px; text-align: right; }

  .web-contact { position: absolute; left: 0; right: 0; top: 246px; text-align: center; font-size: 18px; line-height: 1.45; }
</style>
</head>
<body>
<main class="sheet">

  <section class="card card--front-a" aria-label="Front of card, Marieke de Boeckx">
    <div class="brand brand--small"><span class="brand__dot"></span><span class="brand__rule"></span><span class="brand__name">Tranquil Pathway</span></div>
    <div class="holder">
      <h1 class="holder__name">Marieke de Boeckx</h1>
      <p class="holder__role">Professional Clinical Hypnotherapist</p>
    </div>
    <div class="contact contact--personal">
      <p>Mobile: 0467 290 518</p>
      <p>Marieke@TranquilPathway.example.au</p>
    </div>
    <address class="contact contact--rooms" style="font-style:normal">
      Consulting Rooms (Near Lindqvist Hospital)<br>
      482 Brackenfield Road<br>
      Dunmore VIC 3987
    </address>
  </section>

  <section class="card card--back-a" aria-label="Back of card">
    <div class="brand brand--large"><span class="brand__dot"></span><span class="brand__rule"></span><span class="brand__name">Tranquil Pathway</span></div>
    <div class="web-contact">
      <p>Website: www.TranquilPathway.example.au</p>
      <p>Phone: 1300 958 471</p>
    </div>
  </section>

  <section class="card card--front-b" aria-label="Front of card, Colin Marchetti">
    <div class="brand brand--small"><span class="brand__dot"></span><span class="brand__rule"></span><span class="brand__name">Tranquil Pathway</span></div>
    <div class="holder">
      <h1 class="holder__name">Colin Marchetti</h1>
      <p class="holder__role">Professional Clinical Hypnotherapist</p>
    </div>
    <div class="contact contact--personal">
      <p>Mobile: 0455 872 604</p>
      <p>Colin@TranquilPathway.example.au</p>
    </div>
    <address class="contact contact--rooms" style="font-style:normal">
      Consulting Rooms (Near Lindqvist Hospital)<br>
      482 Brackenfield Road<br>
      Dunmore VIC 3987
    </address>
  </section>

  <section class="card card--back-b" aria-label="Back of card">
    <div class="brand brand--large"><span class="brand__dot"></span><span class="brand__rule"></span><span class="brand__name">Tranquil Pathway</span></div>
    <div class="web-contact">
      <p>Website: www.TranquilPathway.example.au</p>
      <p>Phone: 1300 958 471</p>
    </div>
  </section>

</main>
</body>
</html>
```